Website Header Development

I am after a redesign of the Header of a website www.kaltroweb.com.au.
This project is for the header only, and should fit in with the rest of the site
Target Market(s)
Business
Requirements
Should not have
- Over the top. Keep it simple

```html
<!DOCTYPE html>
<html lang="en">
<head>
<meta charset="utf-8">
<title>Kaltro Energy – Resource Efficiency</title>
<link rel="stylesheet" href="https://fonts.googleapis.com/css2?family=Alegreya:wght@500;700&family=Alegreya+Sans:wght@400;500;700&display=swap">
<style>
  :root {
    --page-bg: #f4f4f4;
    --white: #ffffff;
    --brand-blue: #1f3f9a;
    --brand-blue-dark: #1c3990;
    --nav-green: #1b7a3a;
    --nav-green-light: #328c45;
    --heading-navy: #16197a;
    --text-dark: #1a1a1a;
    --photo-light: #e9eef1;
    --photo-mid: #c7d3dc;
    --field-border: #c9c9c9;
  }
  * { margin: 0; padding: 0; box-sizing: border-box; }
  html, body { width: 1200px; height: 514px; overflow: hidden; }
  body {
    background: var(--page-bg);
    font-family: "Alegreya Sans", sans-serif;
    color: var(--text-dark);
    position: relative;
  }
  .site {
    position: absolute; left: 84px; top: 0;
    width: 1035px; height: 514px;
    background: var(--white);
    overflow: hidden;
  }
  .masthead { position: absolute; left: 0; top: 0; width: 1035px; height: 115px; }
  .masthead-rule {
    position: absolute; left: 0; top: 0; width: 560px; height: 5px;
    background: var(--brand-blue);
  }
  .masthead-artwork {
    position: absolute; left: 520px; top: 0; width: 515px; height: 115px;
    background: linear-gradient(90deg, rgba(31,63,154,0) 0%, rgba(31,63,154,0.55) 30%, var(--brand-blue) 60%, var(--brand-blue-dark) 100%);
  }
  .brand {
    position: absolute; left: 59px; top: 44px;
    display: flex; align-items: center; gap: 14px;
  }
  .brand-name {
    font-weight: 700; font-size: 36px;
    color: var(--brand-blue); line-height: 1;
  }
  .brand-mark { width: 30px; height: 30px; background: var(--brand-blue); }
  .main-nav {
    position: absolute; left: 0; top: 119px; width: 1035px; height: 55px;
    background: var(--nav-green); overflow: hidden;
  }
  .main-nav::before {
    content: ""; position: absolute; left: 300px; top: 0; width: 660px; height: 55px;
    background: var(--nav-green-light);
    clip-path: polygon(0 0, 92% 0, 100% 100%, 6% 100%);
  }
  .nav-item {
    position: absolute; color: var(--white); font-size: 13px; font-weight: 400;
    top: 14px; white-space: nowrap;
  }
  .nav-item.primary { font-size: 15.5px; font-weight: 700; top: 18px; }
  .page-title {
    position: absolute; left: 0; width: 730px; top: 204px; text-align: center;
    font-family: "Alegreya", serif; font-weight: 700; font-size: 27px;
    color: var(--heading-navy); letter-spacing: 0.8px;
  }
  .intro { position: absolute; left: 62px; top: 256px; width: 200px; font-size: 15px; line-height: 26px; }
  .intro p + p { margin-top: 27px; }
  .feature-photo {
    position: absolute; left: 298px; top: 269px; width: 362px; height: 242px;
    background: radial-gradient(ellipse at 62% 40%, var(--photo-mid), var(--photo-light) 70%);
  }
  .search {
    position: absolute; left: 762px; top: 174px; width: 189px; height: 32px;
    border: 1px solid #dcdcdc; display: flex; align-items: center; gap: 6px; padding-left: 8px;
    font-family: Arial, sans-serif; font-size: 14px; color: #9a9a9a;
  }
  .sidebar-title {
    position: absolute; left: 762px; top: 244px; width: 140px;
    font-family: "Alegreya", serif; font-weight: 700; font-size: 21px;
    line-height: 31px; letter-spacing: 2.4px; color: var(--brand-blue);
  }
  .signup-note {
    position: absolute; left: 762px; top: 357px; width: 200px;
    font-size: 11.5px; font-weight: 700; line-height: 26px;
  }
  .signup-field {
    position: absolute; left: 762px; top: 444px; width: 192px; height: 27px;
    border: 1px solid var(--field-border); background: var(--white);
  }
  .signup-note.second { top: 484px; }
</style>
</head>
<body>
  <div class="site">
    <header class="masthead">
      <div class="masthead-rule"></div>
      <div class="masthead-artwork" role="img" aria-label="Decorative blue header swoosh with white curved lines"></div>
      <div class="brand">
        <span class="brand-name">Kaltro Energy</span>
        <span class="brand-mark"></span>
      </div>
    </header>

    <nav class="main-nav">
      <span class="nav-item primary" style="left:81px">Home</span>
      <span class="nav-item" style="left:163px">About Us</span>
      <span class="nav-item" style="left:247px">Services</span>
      <span class="nav-item" style="left:322px">Projects and Case Studies</span>
      <span class="nav-item primary" style="left:491px">Financial Information</span>
      <span class="nav-item" style="left:674px">News</span>
      <span class="nav-item" style="left:735px">Contact</span>
    </nav>

    <h1 class="page-title">Resource Efficiency – Sustainable Solutions</h1>

    <div class="intro">
      <p>Is your business performing as well as your competitors?</p>
      <p>Are your fixed costs comparable to industry leaders?</p>
      <p>Is your business becoming less profitable with increased energy, waste and water prices?</p>
    </div>

    <div class="feature-photo" role="img" aria-label="Photo of a businessman fitting a puzzle piece labelled Solution"></div>

    <div class="search">
      <svg width="14" height="14" viewBox="0 0 14 14" aria-hidden="true"><circle cx="8.5" cy="5.5" r="4" fill="none" stroke="#9a9a9a" stroke-width="2"/><path d="M5.5 8.5 L1.5 12.5" stroke="#9a9a9a" stroke-width="2.5" stroke-linecap="round"/></svg>
      <span>Search</span>
    </div>

    <h2 class="sidebar-title">Kaltro Energy Newsletter</h2>
    <p class="signup-note">Would you like to receive our regular monthly Newsletter? Please fill in your Name:</p>
    <div class="signup-field"></div>
    <p class="signup-note second">Let us know your email address so we</p>
  </div>
</body>
</html>
```